Business Card Design Project

We need a business card designed for a new Luxury Custom Homebuilding company based in Arizona. We previous were called "Brellcrest Estates" but want to start using "Brellcrest Custom Homes" We want the message to communicate high end, luxury and cutting-edge. We like the blue, white and black color scheme.
Brellcrest Custom Homes
Marcus T. Pellingham
Chief Executive Officer
Office: 480-555-0142
Mobile: 480-555-0173
email: marcus@brellcrestcustom.com
web adress: www.BrellcrestCustom.com
Updates
We have made a change to our website address and email address based on recieving feedback from a nmber of individuals. The feedback was web address and email address was to long. Therefore we have made a change. The new web adress and email adress are the following.
www.BrellcrestCustom.com
marcus@brellcrestcustom.com
Also I decided against using in yellow. I like the colors blue,black, white and maybe gray.
Target Market(s)
Our target market is the wealthy individuals looking for a luxury high-end custom home.
Industry/Entity Type
Business
Look and feel
Each slider illustrates characteristics of the customer's brand and the style your logo design should communicate.

```html
<!DOCTYPE html>
<html lang="en">
<head>
<meta charset="utf-8">
<title>Brellcrest Custom Homes – Business Card</title>
<link rel="stylesheet" href="https://fonts.googleapis.com/css2?family=Roboto+Condensed:ital,wght@0,400;0,700;1,400;1,700&display=swap">
<style>
  :root {
    --page: #ffffff;
    --panel-light: #e6e7e8;
    --panel-dark: #58585a;
    --ink: #0d0d0d;
    --white: #ffffff;
    --blue: #5b9bd5;
  }
  * { margin: 0; padding: 0; box-sizing: border-box; }
  html, body {
    width: 1200px; height: 1200px; overflow: hidden;
    background: var(--page);
    font-family: "Roboto Condensed", "Arial Narrow", sans-serif;
  }
  .card {
    position: absolute;
    width: 955px; height: 545px;
    overflow: hidden;
    background: var(--panel-light);
  }
  .card--front { left: 114px; top: 14px; }
  .card--back { left: 111px; top: 620px; }
  .card__panels { position: absolute; inset: 0; width: 100%; height: 100%; }
  .panel-light { fill: var(--panel-light); }
  .panel-dark { fill: var(--panel-dark); }

  .brand { position: absolute; color: var(--ink); font-weight: 700; line-height: 0.9; }
  .brand--front { left: 40px; top: 130px; width: 340px; text-align: right; }
  .brand--front .brand__name { display: block; font-size: 80px; letter-spacing: -3px; }
  .brand--front .brand__tag { display: block; font-size: 34px; text-transform: uppercase; margin-top: 2px; }

  .contact { position: absolute; left: 567px; color: var(--white); }
  .contact__name { position: absolute; top: 136px; font-size: 30px; font-weight: 700; white-space: nowrap; }
  .contact__title { position: absolute; top: 175px; font-size: 22px; white-space: nowrap; }
  .contact__lines { position: absolute; top: 315px; list-style: none; font-size: 22px; line-height: 32px; white-space: nowrap; }
  .contact__lines span { display: inline-block; width: 40px; }

  .web {
    position: absolute; color: var(--white);
    font-size: 28px; font-style: italic; white-space: nowrap;
  }
  .web b { font-weight: 700; }
  .web .web__accent { color: var(--blue); font-weight: 700; }
  .card--front .web { left: 567px; top: 478px; }
  .card--back .web { left: 466px; top: 476px; }

  .brand--back { left: 0; top: 120px; width: 955px; text-align: center; }
  .brand--back .brand__name { display: block; font-size: 220px; letter-spacing: -6px; line-height: 0.85; }
  .brand--back .brand__tag { position: absolute; right: 30px; top: 200px; font-size: 76px; text-transform: uppercase; white-space: nowrap; }
</style>
</head>
<body>
  <section class="card card--front" aria-label="Card front">
    <svg class="card__panels" viewBox="0 0 955 545" preserveAspectRatio="none" aria-hidden="true">
      <rect class="panel-light" width="955" height="545"/>
      <path class="panel-dark" d="M418 0 Q455 270 410 545 L955 545 L955 0 Z"/>
    </svg>
    <div class="brand brand--front">
      <span class="brand__name">Brellcrest</span>
      <span class="brand__tag">Custom Homes</span>
    </div>
    <div class="contact">
      <p class="contact__name">Marcus T. Pellingham</p>
      <p class="contact__title">Chief Executive Officer</p>
      <ul class="contact__lines">
        <li><span>P:</span>480-555-0142</li>
        <li><span>M:</span>480-555-0173</li>
        <li><span>E:</span>marcus@brellcrestcustom.com</li>
      </ul>
    </div>
    <p class="web">www.<b>Brellcrest</b><span class="web__accent">Custom</span>.com</p>
  </section>

  <section class="card card--back" aria-label="Card back">
    <svg class="card__panels" viewBox="0 0 955 545" preserveAspectRatio="none" aria-hidden="true">
      <rect class="panel-light" width="955" height="545"/>
      <path class="panel-dark" d="M320 0 Q335 270 300 545 L955 545 L955 0 Z"/>
    </svg>
    <div class="brand brand--back">
      <span class="brand__name">Brellcrest</span>
      <span class="brand__tag">Custom Homes</span>
    </div>
    <p class="web">www.<b>Brellcrest</b><span class="web__accent">Custom</span>.com</p>
  </section>
</body>
</html>
```